Best local air conditioning and heating contractor

We need a website design for a new company in Tampa Bay called the Summit Breeze Cooling Company. We provide superior services for residential and commercial properties as well as maintenance and installing HVAC systems. We also want to sell equipment, parts and filter on the website as well. We want it easy to use for customers. Rich with content and keywords for our area.

Target Market(s)

homeowners in Tampa Bay

Industry/Entity Type

HVAC air conditioning and heating

Coding

Coded - Design and coding required

Number of Pages Required

5+ page

Font styles to use
Sans Serif

Requirements
Nice to have
• would like the colors to be same as logo

```html
<!DOCTYPE html>
<html lang="en">
<head>
<meta charset="utf-8">
<title>Summit Breeze Cooling Company</title>
<link href="https://fonts.googleapis.com/css2?family=Oswald:wght@500;600&family=Roboto:wght@400;500;700&display=swap" rel="stylesheet">
<style>
:root{
  --red:#d62027;
  --navy:#1f2d6b;
  --navy-deep:#1a2659;
  --ink:#222;
  --gray-bg:#efefef;
  --muted:#555;
  --white:#fff;
}
*{margin:0;padding:0;box-sizing:border-box}
html,body{width:1200px;height:5106px;overflow:hidden}
body{position:relative;font-family:Roboto,Arial,sans-serif;color:var(--ink);background:var(--white)}
.abs{position:absolute}
.head{font-family:Oswald,Arial,sans-serif;font-weight:600;text-transform:uppercase;letter-spacing:.3px}
.btn{position:absolute;display:flex;align-items:center;justify-content:center;font-family:Oswald,Arial,sans-serif;font-weight:500;color:#fff;text-transform:uppercase;font-size:16px}
.btn-red{background:var(--red)}
.btn-navy{background:var(--navy)}
.red{color:var(--red)}
.navy{color:var(--navy)}

/* header */
.site-header{top:0;left:0;width:1200px;height:130px;background:#fff}
.brand{left:90px;top:34px;width:250px;font-family:Oswald,Arial,sans-serif;font-weight:600;font-size:22px;line-height:26px;color:var(--navy);text-transform:uppercase}
.brand-dot{display:inline-block;width:14px;height:14px;background:var(--red);margin-right:8px;vertical-align:middle}
.call{left:745px;top:28px;font-family:Oswald,Arial,sans-serif;font-size:20px;font-weight:500;color:var(--red);display:flex;align-items:center;gap:8px}
.nav{top:90px;left:0;width:1200px;height:24px;font-family:Oswald,Arial,sans-serif;font-size:15px;font-weight:500;color:#333;text-transform:uppercase}
.nav span{position:absolute;top:0}
.nav .active{color:var(--red)}

/* hero */
.hero{top:130px;left:0;width:1200px;height:593px;background:linear-gradient(100deg,#4a5a7e 0%,#7a6a5a 40%,#8b7563 70%,#6c5a4d 100%)}
.hero-title{left:677px;top:280px;font-size:52px;line-height:54px;color:#fff}

/* services */
.services{top:723px;left:0;width:1200px;height:635px;background:var(--gray-bg)}
.section-title{position:absolute;left:0;width:1200px;text-align:center;font-size:46px;color:var(--navy)}
.card{position:absolute;background:#fff;box-shadow:0 0 6px rgba(0,0,0,.12)}
.card .photo{position:absolute;left:0;top:0;width:100%}
.card h3{position:absolute;left:0;width:100%;text-align:center;font-size:24px;color:var(--navy)}
.card p{position:absolute;left:20px;right:20px;text-align:center;font-size:14px;line-height:19px;color:var(--muted)}

/* about */
.about-photo{left:100px;top:1457px;width:456px;height:456px;border-radius:50%;border:3px solid var(--red);padding:10px}
.about-photo div{width:100%;height:100%;border-radius:50%;background:linear-gradient(160deg,#6f8a5a,#243266 55%,#a9a9a6)}
.body-copy{font-size:14.5px;line-height:18.5px;color:#222}

/* why */
.why{top:1988px;left:0;width:1200px;height:610px;background:linear-gradient(90deg,#1c2a60,#24346e 50%,#1c2a60)}
.feature h4{font-family:Roboto,Arial,sans-serif;font-weight:700;font-size:19px;color:#fff;text-transform:uppercase;margin-bottom:6px}
.feature p{font-size:14px;line-height:18px;color:#c9cfe3}

/* blog */
.blog-card p{font-weight:700;font-size:18px;line-height:20px;color:#111}
/* footer */
.footer{top:4700px;left:0;width:1200px;height:406px;background:var(--navy)}
.footer h5{font-family:Oswald,Arial,sans-serif;font-weight:500;font-size:18px;color:var(--red);text-transform:uppercase}
.footer .link{font-size:15px;color:#fff;line-height:26.5px}
.field{position:absolute;background:#fff;font-size:14px;color:#666;padding:12px 14px}
</style>
</head>
<body>

<header class="site-header abs">
  <div class="brand abs"><span class="brand-dot"></span>Summit Breeze<br>Cooling Company</div>
  <div class="call abs">
    <svg width="20" height="20" viewBox="0 0 24 24"><path fill="#d62027" d="M6.6 10.8a15 15 0 0 0 6.6 6.6l2.2-2.2c.3-.3.7-.4 1-.2 1.1.4 2.3.6 3.6.6.6 0 1 .4 1 1V20c0 .6-.4 1-1 1A17 17 0 0 1 3 4c0-.6.4-1 1-1h3.5c.6 0 1 .4 1 1 0 1.3.2 2.5.6 3.6.1.3 0 .7-.2 1z"/></svg>
    CALL: 55 555 0142
  </div>
  <div class="btn btn-red" style="left:968px;top:20px;width:146px;height:42px;font-size:15px">Get a Quote</div>
  <nav class="nav abs">
    <span class="active" style="left:428px">Home</span>
    <span style="left:518px">Services</span>
    <span style="left:635px">About Us</span>
    <span style="left:762px">Gallery</span>
    <span style="left:882px">Service Area</span>
    <span style="left:1032px">Contact Us</span>
  </nav>
</header>

<section class="hero abs" role="img" aria-label="Smiling technician servicing an outdoor air conditioning unit">
</section>
<h1 class="hero-title abs head">Welcome to<br><span class="red">Summit Breeze</span><br>Cooling<br>Company</h1>
<div class="btn btn-red" style="left:678px;top:518px;width:160px;height:47px">Get a Quote</div>

<section class="services abs">
  <h2 class="section-title head" style="top:63px"><span class="red">Our</span> Services</h2>
  <div class="card" style="left:125px;top:162px;width:295px;height:395px">
    <div class="photo" role="img" aria-label="Technician installing a condenser unit" style="height:230px;background:linear-gradient(135deg,#c8ccd0,#8a9aa8 60%,#d9c24a)"></div>
    <h3 class="head" style="top:250px">Air Conditioning</h3>
    <p style="top:310px">Lorem ipsum dolor sit amet, consectetur adipiscing elitseo eiusmod tempor inciore</p>
  </div>
  <div class="card" style="left:454px;top:162px;width:296px;height:395px">
    <div class="photo" role="img" aria-label="Hands holding refrigerant pressure gauges" style="height:230px;background:linear-gradient(135deg,#9aa3ad,#5d6a7a 55%,#b8b2a8)"></div>
    <h3 class="head" style="top:250px">Heating</h3>
    <p style="top:310px">Lorem ipsum dolor sit amet, consectetur adipiscing elitseo eiusmod tempor inciore</p>
  </div>
  <div class="card" style="left:779px;top:162px;width:295px;height:395px">
    <div class="photo" role="img" aria-label="Technician servicing an indoor split air conditioner" style="height:230px;background:linear-gradient(135deg,#e8ecef,#c9d0d6 60%,#a8b0b8)"></div>
    <h3 class="head" style="top:250px">Indoor Air Quality</h3>
    <p style="top:310px">Lorem ipsum dolor sit amet, consectetur adipiscing elitseo eiusmod tempor inciore</p>
  </div>
</section>

<div class="about-photo abs"><div role="img" aria-label="Technician repairing an outdoor unit with a tool bag"></div></div>
<h2 class="abs head navy" style="left:652px;top:1488px;font-size:46px">About <span class="red">Us</span></h2>
<p class="abs body-copy" style="left:652px;top:1565px;width:430px">Lorem ipsum dolor sit amet, consectetur adipiscing elit, sed do eiusmod tempor incididunt ut labore et dolore magna aliqua. Quis ipsum suspendisse ultrices gravida. Risus commodo viverra maecenas accumsan lacus vel facilisis.</p>
<p class="abs body-copy" style="left:652px;top:1657px;width:430px">Lorem ipsum dolor sit amet, consectetur adipiscing elit, sed do eiusmod tempor incididunt ut labore et dolore magna aliqua. Quis ipsum suspendisse ultrices gravida. Risus commloreodo viverra maecenas accumsan lacus vel facilisis. uislore ipsum suspendisse ultrices gravida. Risus commodo vilore,verra maecenas accumsan lacus vel facilisis.</p>
<div class="btn btn-red" style="left:651px;top:1788px;width:142px;height:52px;font-size:15px">Read More</div>

<section class="why abs">
  <h2 class="section-title head" style="top:82px;color:#fff;font-size:42px">Why Choose Us?</h2>
  <div class="abs" style="left:475px;top:205px;width:250px;height:250px;border-radius:50%;background:#fff;border:8px solid var(--red)">
    <div class="abs" style="left:58px;top:85px;width:118px;height:64px;border-radius:32px;background:var(--red)"></div>
  </div>
  <div class="feature abs" style="left:60px;top:205px;width:290px;text-align:right">
    <h4>Financing &amp; Pricing</h4><p>Lorem ipsum dolor sit amet, consec adipiscing elit, sed do eiusmod tempor incididunt ut labore et dolore.</p>
  </div>
  <div class="feature abs" style="left:60px;top:372px;width:290px;text-align:right">
    <h4>Same Day Service</h4><p>Lorem ipsum dolor sit amet, consec adipiscing elit, sed do eiusmod tempor incididunt ut labore et dolore.</p>
  </div>
  <div class="feature abs" style="left:868px;top:205px;width:275px">
    <h4>Good Technicians</h4><p>Lorem ipsum dolor sit amet, consec adipiscing elit, sed do eiusmod tempor incididunt ut labore et dolore.</p>
  </div>
  <div class="feature abs" style="left:868px;top:372px;width:275px">
    <h4>Guaranteed</h4><p>Lorem ipsum dolor sit amet, consec adipiscing elit, sed do eiusmod tempor incididunt ut labore et dolore.</p>
  </div>
  <svg class="abs" style="left:372px;top:215px" width="80" height="60" viewBox="0 0 80 60" fill="none" stroke="#fff" stroke-width="2.5"><rect x="8" y="14" width="60" height="36" rx="3"/><circle cx="38" cy="32" r="8" stroke="#d62027"/><path d="M16 8h56v36"/></svg>
  <svg class="abs" style="left:372px;top:380px" width="70" height="70" viewBox="0 0 70 70" fill="none" stroke="#fff" stroke-width="2.5"><circle cx="38" cy="40" r="22"/><path d="M38 40V28M38 40l8 6" stroke="#d62027"/><path d="M32 12h12M4 34h12M2 44h14"/></svg>
  <svg class="abs" style="left:768px;top:210px" width="75" height="70" viewBox="0 0 75 70" fill="none" stroke="#fff" stroke-width="2.5"><path d="M10 8l10 10v40h8V18l10-10"/><path d="M44 10v50"/><circle cx="58" cy="26" r="10" stroke="#d62027"/><circle cx="58" cy="26" r="4" stroke="#d62027"/></svg>
  <svg class="abs" style="left:768px;top:372px" width="80" height="75" viewBox="0 0 80 75" fill="none" stroke="#fff" stroke-width="2.5"><circle cx="46" cy="22" r="16" stroke="#d62027"/><path d="M38 22l6 6 10-12" stroke="#d62027"/><path d="M4 50h14l16 6h20l14-10M18 50v20"/></svg>
</section>

<section class="abs" style="top:2598px;left:0;width:1200px;height:377px;background:linear-gradient(120deg,#6d6f73,#b9bcbf 40%,#8a8d91)" role="img" aria-label="Outdoor condenser units beside a house wall"></section>
<svg class="abs" style="top:2598px;left:0" width="1200" height="377"><polygon points="740,0 1200,0 1200,377 635,377 635,140" fill="#d62027"/></svg>
<h2 class="abs head" style="left:700px;top:2714px;width:460px;text-align:center;color:#fff;font-size:40px;line-height:42px">Same Day Service<br>Available Call Now!</h2>
<div class="btn btn-navy" style="left:862px;top:2842px;width:135px;height:51px;font-size:15px">Call Now</div>

<h2 class="section-title head" style="top:3060px;font-size:46px;color:#111">Latest Blog <span class="red">Posts</span></h2>
<svg class="abs" style="left:74px;top:3245px" width="24" height="34" viewBox="0 0 24 34"><path d="M18 3L5 17l13 14" fill="none" stroke="#888" stroke-width="3"/></svg>
<svg class="abs" style="left:1100px;top:3245px" width="24" height="34" viewBox="0 0 24 34"><path d="M6 3l13 14L6 31" fill="none" stroke="#888" stroke-width="3"/></svg>
<div class="card blog-card" style="left:128px;top:3157px;width:295px;height:321px">
  <div class="photo" role="img" aria-label="Two technicians working on an outdoor unit" style="height:210px;background:linear-gradient(135deg,#8b5a45,#2a3b72 55%,#a9a9a6)"></div>
  <p class="abs" style="left:20px;right:20px;top:247px;text-align:center">Lorem ipsum dolor sit ameconsect.</p>
</div>
<div class="card blog-card" style="left:454px;top:3157px;width:295px;height:321px">
  <div class="photo" role="img" aria-label="Technician installing a wall air conditioner while a client watches" style="height:210px;background:linear-gradient(135deg,#e6e4e2,#c9c7c4 55%,#2c5aa8)"></div>
  <p class="abs" style="left:20px;right:20px;top:247px;text-align:center">Lorem ipsum dolor sit ameconsect.</p>
</div>
<div class="card blog-card" style="left:778px;top:3157px;width:295px;height:321px">
  <div class="photo" role="img" aria-label="Technician in red servicing an outdoor unit" style="height:210px;background:linear-gradient(135deg,#5a7a3a,#e4e6e8 50%,#c3252a)"></div>
  <p class="abs" style="left:20px;right:20px;top:247px;text-align:center">Lorem ipsum dolor sit ameconsect.</p>
</div>

<section class="abs" style="top:3580px;left:0;width:1200px;height:530px;background:var(--gray-bg)">
  <h2 class="abs head navy" style="left:128px;top:190px;font-size:44px">Service <span class="red">Areas</span></h2>
  <p class="abs body-copy" style="left:128px;top:275px;width:410px;font-size:14px;line-height:18.5px">Lorem ipsum dolor sit amet, consectetur adipiscing elit, sed do eiusmod tempor incididunt ut labore et dolore magna aliqua. Quis ipsum suspendisse ultrices gravida. Risus commodo viverra maecenas accumsan lacus vel facilisis. Lorem ipsum dolor sit amet, consectetur adipiscing elit, sed do eiusmod tempor incididunt ut labore et dolo</p>
  <div class="abs" role="img" aria-label="Regional map with service location pins" style="left:625px;top:85px;width:430px;height:395px;border-radius:40% 45% 40% 35%;background:radial-gradient(circle,#c9c9c9,#d8d8d8 70%)"></div>
</section>

<section class="abs" role="img" aria-label="Two smiling technicians in front of a brick wall" style="top:4110px;left:0;width:1200px;height:590px;background:linear-gradient(100deg,#6e4638,#2a3a78 35%,#5a3a30 60%,#7a4a3a)"></section>
<div class="abs" style="left:703px;top:4205px;width:363px;height:483px;background:var(--red)">
  <h2 class="abs head" style="left:0;width:100%;top:30px;text-align:center;color:#fff;font-size:32px">Get a Quote</h2>
  <div class="field" style="left:39px;top:97px;width:289px;height:44px">Name</div>
  <div class="field" style="left:39px;top:153px;width:289px;height:44px">Email:</div>
  <div class="field" style="left:39px;top:209px;width:289px;height:44px">Phone:</div>
  <div class="field" style="left:39px;top:265px;width:289px;height:118px">Message:</div>
  <div class="btn btn-navy" style="left:110px;top:364px;width:122px;height:32px;font-size:14px">Submit</div>
</div>

<footer class="footer abs">
  <div class="abs" style="left:128px;top:62px;width:230px;font-family:Oswald,Arial,sans-serif;font-weight:600;font-size:21px;line-height:25px;color:#fff;text-transform:uppercase">Summit Breeze<br>Cooling Company</div>
  <div class="abs" style="left:150px;top:172px;display:flex;gap:13px">
    <span style="width:32px;height:32px;border-radius:50%;border:2px solid #fff"></span>
    <span style="width:32px;height:32px;border-radius:50%;border:2px solid #fff"></span>
    <span style="width:32px;height:32px;border-radius:50%;border:2px solid #fff"></span>
    <span style="width:32px;height:32px;border-radius:50%;border:2px solid #fff"></span>
  </div>
  <h5 class="abs" style="left:398px;top:66px">Links</h5>
  <div class="abs" style="left:398px;top:117px">
    <div class="link">About</div><div class="link">Services</div><div class="link">Products</div><div class="link">Recent Projects</div><div class="link">Service Area Map</div><div class="link">About Us</div>
  </div>
  <h5 class="abs" style="left:562px;top:66px">Contact Us</h5>
  <svg class="abs" style="left:553px;top:128px" width="40" height="140" viewBox="0 0 40 140" fill="none" stroke="#fff" stroke-width="2">
    <circle cx="20" cy="20" r="17"/><path d="M20 13a5 5 0 0 1 5 5c0 4-5 10-5 10s-5-6-5-10a5 5 0 0 1 5-5z"/>
    <circle cx="20" cy="75" r="17"/><path d="M14 69l3-2 3 4-2 2a9 9 0 0 0 5 5l2-2 4 3-2 3c-7 0-13-6-13-13z"/>
    <circle cx="20" cy="124" r="17"/><rect x="12" y="118" width="16" height="12"/><path d="M12 118l8 7 8-7"/>
  </svg>
  <div class="abs link" style="left:602px;top:120px;font-size:14.5px;line-height:18px">Location Name<br>2210 Bayview Lane<br>Tampa FL 33600</div>
  <div class="abs link" style="left:602px;top:190px;font-size:14.5px">Phone:555.010.0188</div>
  <div class="abs link" style="left:602px;top:239px;font-size:14.5px">hello@summitbreeze.example</div>
  <h5 class="abs" style="left:815px;top:66px">Newsletter Sign Up</h5>
  <p class="abs" style="left:815px;top:118px;width:255px;font-size:14px;line-height:18px;color:#fff">Lorem ipsum dolor sit amelor conse ctet ur adipisclorem ipsumilited do eiusmod tempor incididu.</p>
  <div class="field" style="left:815px;top:200px;width:239px;height:46px;font-size:13px;color:#999">Email</div>
  <svg class="abs" style="left:1007px;top:216px" width="34" height="14" viewBox="0 0 34 14"><path d="M0 7h31M25 1l6 6-6 6" fill="none" stroke="#333" stroke-width="2"/></svg>
  <div class="abs" style="left:100px;top:340px;width:1000px;height:1px;background:rgba(255,255,255,.3)"></div>
  <p class="abs" style="left:0;top:368px;width:1200px;text-align:center;font-size:14px;color:#fff">© 2024 All Rights Reserved.Terms &amp; Conditions Privacy Policy</p>
</footer>

</body>
</html>
```